Security Warning Sign

We have an existing sign that needs an update. I have attached a picture of the current square sign. We need to maintain the same wording. It needs to be professional and appropriate to attach to our customers fence. Also attached is a copy of our building sign which may lend some inspiration and hopefully the ai format will assist. The final sign will be 600mm x 600mmOur website is www.halvorngate.com.au

```html
<!DOCTYPE html>
<html lang="en">
<head>
<meta charset="utf-8">
<title>Security Warning Sign</title>
<link href="https://fonts.googleapis.com/css2?family=Stardos+Stencil:wght@700&family=League+Spartan:wght@700&family=Open+Sans:wght@800&display=swap" rel="stylesheet">
<style>
  :root {
    --sign-dark: #222223;
    --sign-dark-2: #2c2c2d;
    --warning-red: #ed1c24;
    --warning-yellow: #ffe500;
    --ink: #231f20;
    --white: #ffffff;
    --brand-orange: #f3811f;
    --band-grey: #4b4b4c;
  }
  * { margin: 0; padding: 0; box-sizing: border-box; }
  html, body { width: 1200px; height: 1200px; overflow: hidden; background: var(--sign-dark); }
  .sign {
    position: relative;
    width: 1200px;
    height: 1200px;
    overflow: hidden;
    background: linear-gradient(135deg, var(--sign-dark-2) 0%, var(--sign-dark) 45%, var(--sign-dark-2) 70%, var(--sign-dark) 100%);
  }
  .headline-bar {
    position: absolute;
    left: 60px; top: 68px;
    width: 1080px; height: 171px;
    background: var(--white);
    border-radius: 86px;
  }
  .hazard-icon {
    position: absolute;
    left: 140px; top: 86px;
    width: 156px; height: 136px;
  }
  .headline {
    position: absolute;
    left: 316px; top: 74px;
    width: 750px;
    font-family: "Stardos Stencil", "Black Ops One", fantasy;
    font-weight: 700;
    font-size: 132px;
    line-height: 160px;
    color: var(--warning-red);
    text-align: center;
    letter-spacing: 0;
  }
  .notice-panel {
    position: absolute;
    left: 60px; top: 268px;
    width: 1080px; height: 607px;
    background: var(--warning-yellow);
    border-radius: 62px;
  }
  .notice-text {
    position: absolute;
    left: 60px; top: 296px;
    width: 1080px;
    font-family: "League Spartan", "Arial Black", sans-serif;
    font-weight: 700;
    font-size: 116px;
    line-height: 111px;
    color: var(--ink);
    text-align: center;
    letter-spacing: -1px;
    text-transform: uppercase;
  }
  .brand-dot {
    position: absolute;
    left: 90px; top: 935px;
    width: 150px; height: 150px;
    border-radius: 50%;
    background: var(--brand-orange);
  }
  .brand-name {
    position: absolute;
    left: 292px; top: 922px;
    font-family: "Open Sans", Arial, sans-serif;
    font-weight: 800;
    font-size: 58px;
    line-height: 57px;
    color: var(--white);
    text-transform: uppercase;
  }
  .footer-art {
    position: absolute;
    left: 0; top: 0;
    width: 1200px; height: 1200px;
  }
  .website {
    position: absolute;
    left: 62px; top: 1146px;
    font-family: "Open Sans", Arial, sans-serif;
    font-weight: 800;
    font-size: 30px;
    line-height: 46px;
    color: var(--white);
    text-transform: uppercase;
  }
  .phone {
    position: absolute;
    left: 742px; top: 1132px;
    display: flex;
    align-items: center;
    gap: 14px;
    font-family: "Open Sans", Arial, sans-serif;
    font-weight: 800;
    font-size: 45px;
    line-height: 66px;
    color: var(--white);
  }
  .phone svg { width: 46px; height: 46px; }
</style>
</head>
<body>
<main class="sign">
  <div class="headline-bar"></div>
  <svg class="hazard-icon" viewBox="0 0 156 136" aria-hidden="true">
    <polygon points="78,4 152,131 4,131" fill="#ffe500" stroke="#ffe500" stroke-width="6" stroke-linejoin="round"/>
    <polygon points="78,16 142,125 14,125" fill="none" stroke="#231f20" stroke-width="6" stroke-linejoin="round"/>
    <path d="M70 44 h16 l-4 48 h-8 z" fill="#231f20"/>
    <circle cx="78" cy="106" r="8" fill="#231f20"/>
  </svg>
  <h1 class="headline">WARNING</h1>

  <div class="notice-panel"></div>
  <p class="notice-text">Electronic<br>Surveillance<br>and Recording<br>Devices Installed<br>in this Area</p>

  <div class="brand-dot"></div>
  <p class="brand-name">Halvorngate<br>Security<br>Services</p>

  <svg class="footer-art" viewBox="0 0 1200 1200" aria-hidden="true">
    <polygon points="0,1146 688,1146 658,1200 0,1200" fill="#4b4b4c"/>
    <polygon points="690,1146 700,1146 670,1200 660,1200" fill="#6a6a6b"/>
    <polygon points="708,1130 716,1130 677,1200 669,1200" fill="#6a6a6b"/>
    <polygon points="728,1115 1200,1115 1200,1200 680,1200" fill="#f3811f"/>
  </svg>
  <p class="website">www.halvorngate.com.au</p>
  <p class="phone">
    <svg viewBox="0 0 48 48" aria-hidden="true">
      <path d="M14 8 l7 9 -4 5 c2 5 6 9 11 11 l5 -4 9 7 -4 6 c-14 0 -28 -14 -28 -28 z" fill="#ffffff"/>
      <path d="M26 6 a16 16 0 0 1 16 16" fill="none" stroke="#ffffff" stroke-width="3"/>
      <path d="M26 13 a9 9 0 0 1 9 9" fill="none" stroke="#ffffff" stroke-width="3"/>
    </svg>
    1300 555 014
  </p>
</main>
</body>
</html>
```